I have a business that exists already (Belvina Conservatory of Music) that we offer music lessons to all instruments. I recently opened a smaller version called TONES by Belvina that will only teach piano lessons. What I'm looking for now is a 3 page Website on word press. After I choose the design I like I want to be able to take over the website and bring it to our hosting company. We want full control of it and our team will take over. The reason I'm doing this is to have other visions and ideas from others. The first page will be about the company and our message/vision. Second page about the piano lessons. The third will be about franchising this concept "Tones by Belvina" Attached are 3 Logos . Please refer to our existing website www.belvinamusicschool-example.com to look at our piano page and franchising page. Please feel free to message me if you need more info. Thanks
Please note I do not want the new website (Tones by Belvina) To look like the other Website (Belvina Conservatory of Music) Fresh new look. I do not want the colours red or using the Red logo. I only provided it so that you have an Idea of What the other business looks like and that you can take the piano content and franchise content off of it. Tones by Belvina is smaller concept and only piano lessons.
Thanks
Only Piano lessons for all students
3 page

```html
<!DOCTYPE html>
<html lang="en">
<head>
<meta charset="utf-8">
<title>Tones by Belvina — Piano Lessons</title>
<link rel="stylesheet" href="https://fonts.googleapis.com/css2?family=Cinzel:wght@400;700&family=Lora:ital,wght@0,400;0,700;1,400&family=Montserrat:wght@400&display=swap">
<style>
:root{
  --teal:#5bc5b9;
  --blue:#2196f3;
  --ink:#1c1c1c;
  --text:#333;
  --sand:#f0eeea;
  --black:#000;
  --white:#fff;
}
*{box-sizing:border-box;margin:0;padding:0}
html,body{width:1200px;height:2845px;overflow:hidden;background:var(--white)}
body{font-family:'Lora',Georgia,serif;color:var(--text)}
.page{position:relative;width:1200px;height:2845px;overflow:hidden}
.abs{position:absolute}

/* header */
.site-header{left:0;top:0;width:1200px;height:93px;background:var(--white)}
.brand{left:143px;top:22px;display:flex;align-items:center;gap:10px;font-family:'Lora',serif;font-size:28px;color:var(--ink);letter-spacing:1px}
.brand-mark{width:14px;height:14px;background:var(--ink)}
.brand small{font-size:15px;letter-spacing:0}
.main-nav{right:140px;top:36px;display:flex;gap:36px;font-family:'Lora',serif;font-size:13.5px;letter-spacing:1.3px;color:#222}
.main-nav .active{color:var(--blue)}

/* hero */
.hero{left:0;top:93px;width:1200px;height:479px;background:linear-gradient(90deg,#b98a62 0%,#d9c6b3 22%,#eeebe7 45%,#f3f1ef 70%,#e9e6e3 100%)}
.hero-copy{right:145px;top:222px;text-align:right;font-family:'Cinzel',serif;color:var(--ink)}
.hero-copy .l1{font-size:31px;line-height:40px}
.hero-copy .l2{font-size:46px;line-height:58px}
.hero-copy .l3{font-size:31px;line-height:44px}
.btn-hero{right:141px;top:383px;width:184px;height:35px;background:var(--blue);color:var(--white);font-family:'Cinzel',serif;font-size:16px;display:flex;align-items:center;justify-content:center}

/* intro */
.intro{left:0;top:572px;width:1200px;height:571px;background:var(--sand)}
.intro-card{left:141px;top:591px;width:918px;height:421px;background:var(--white)}
.intro-photo{left:141px;top:591px;width:437px;height:421px;background:linear-gradient(135deg,#2e2a28,#8a7463 45%,#e3d7cc 75%,#f5f2ee)}
.intro-text{left:612px;top:628px;width:412px;text-align:center}
.intro-text h2{font-weight:400;font-size:35px;color:var(--ink);margin-bottom:16px}
.intro-text p{font-size:13px;line-height:23px;color:#333;margin-bottom:6px}
.scroll-hint{left:580px;top:1052px}

/* vision */
.section-title{font-weight:400;color:var(--ink)}
.vision-text{left:143px;top:1248px;width:500px}
.vision-text h2{font-size:35px;margin-bottom:10px}
.vision-text p{font-size:12.6px;line-height:25.4px;margin-bottom:6px}
.vision-text .btn-teal{margin-top:14px;margin-left:-2px;width:169px;height:35px}
.btn-teal{background:var(--teal);color:var(--white);font-family:'Lora',serif;font-weight:700;font-size:13px;letter-spacing:.4px;display:flex;align-items:center;justify-content:center}
.frame{background:var(--teal)}
.frame-line{border:1.5px solid var(--white)}
.photo{background:linear-gradient(160deg,#f3ede6,#e6c7b0 45%,#d58f7c 75%,#3b3433)}

/* programs */
.programs{left:576px;top:1660px;width:490px}
.programs h2{font-size:31px;line-height:40px;margin-bottom:12px}
.programs ul{list-style:none}
.programs li{position:relative;padding-left:25px;font-size:14.3px;line-height:22.5px;margin-bottom:9px}
.programs li svg{position:absolute;left:2px;top:6px}

/* quote */
.quote-card{left:141px;top:2147px;width:918px;height:212px;background:var(--white);border-radius:18px;box-shadow:0 2px 14px rgba(0,0,0,.08)}
.quote-text{left:280px;top:2193px;width:640px;text-align:center;font-style:italic;font-size:24px;line-height:39px;color:#333}
.quote-name{left:0;top:2284px;width:1200px;text-align:center;font-weight:700;font-size:18px;color:var(--teal);letter-spacing:.5px}

/* franchise */
.franchise{left:0;top:2425px;width:1200px;text-align:center}
.franchise h2{font-size:46px;margin-bottom:10px}
.franchise p{font-size:20px;letter-spacing:.4px;color:#333}

/* footer */
.site-footer{left:0;top:2646px;width:1200px;height:150px;background:var(--black);color:var(--white)}
.contact-item{top:2690px;display:flex;align-items:center;gap:12px;color:var(--white)}
.contact-item .lbl{font-size:14px;line-height:18px}
.contact-item .big{font-size:20px;line-height:24px}
.divider{top:2703px;width:1px;height:30px;background:#444}
.copy-bar{left:0;top:2796px;width:1200px;height:49px;background:var(--teal)}
.copyright{left:143px;top:2813px;font-family:'Montserrat',sans-serif;font-size:12.5px;color:var(--white)}
.socials{right:141px;top:2806px;display:flex;gap:7px}
.socials span{width:25px;height:25px;border:1.5px solid var(--white);border-radius:50%}
</style>
</head>
<body>
<div class="page">

  <header class="site-header abs">
    <div class="brand abs"><span class="brand-mark"></span>TONES <small>by Belvina</small></div>
    <nav class="main-nav abs">
      <span class="active">HOME</span><span>PIANO LESSONS</span><span>FRANCHISING</span><span>CONTACT US</span>
    </nav>
  </header>

  <section class="hero abs" role="img" aria-label="Teacher and boy playing a white grand piano in a bright room"></section>
  <div class="hero-copy abs">
    <div class="l1">We Provide</div>
    <div class="l2">Piano Lessons</div>
    <div class="l3">For All Students</div>
  </div>
  <div class="btn-hero abs">Contact Us Today</div>

  <section class="intro abs"></section>
  <div class="intro-card abs"></div>
  <div class="intro-photo abs" role="img" aria-label="Close-up of hands playing piano keys"></div>
  <div class="intro-text abs">
    <h2>Playing The Piano</h2>
    <p>When you think of a piano, you probably envision black and white keys but the piano is more than those harmonious sounds created by the player.</p>
    <p>The versatility and the musicianship instilled into the player from those keys is the true magic that comes from playing piano! Starting from the grassroots, experience different methods and styles of playing piano. To mark the milestones of progression, engage in one of Belvina’s many unique performance opportunities like annual festival competitions, recitals or our examinations (Belvina &amp; NPB). Penultimately, at the end of the journey, join our elite teaching program to bring the same joy of learning the piano to another student.</p>
  </div>
  <svg class="scroll-hint abs" width="40" height="40" viewBox="0 0 40 40" aria-hidden="true">
    <rect x="8" y="8" width="24" height="24" transform="rotate(45 20 20)" fill="none" stroke="#d6d3cd" stroke-width="1.5"/>
    <path d="M20 13v13M15 21l5 5 5-5" fill="none" stroke="#c8c5bf" stroke-width="1.5"/>
  </svg>

  <div class="vision-text abs">
    <h2 class="section-title">Our Vision</h2>
    <p>Lorem ipsum dolor sit amet, consectetur adipiscing elit. In hendrerit, odio utrtyy semper consequat, justo dui convallis ligula, ac congue felis ipsum sed felis. Cura volutpat leo faucibus magna elementum ultrices.</p>
    <p>Cras eleifend faucibus lacus convallis elementum. Phasellus vitae lobortis donece in risus sit amet enim eleifend semper sed id ipsum. Ut ac placerat nisl pellentesq venenatis ligula eget turpis aliquam ornare. Vivamus tincidunt tellus at rutrum fd aliquam. Etiam ullamcorper consequat felis vitae posuere. Nunc nec facilisis nuni, at dignissim augue. Sed sed orci felis. Aliquam quis auctor ipsum.</p>
    <div class="btn-teal">CONTACT US TODAY</div>
  </div>
  <div class="frame abs" style="left:741px;top:1222px;width:318px;height:319px"></div>
  <div class="frame-line abs" style="left:741px;top:1240px;width:299px;height:280px;border-left:none;border-bottom:none"></div>
  <div class="photo abs" style="left:678px;top:1284px;width:318px;height:316px" role="img" aria-label="Teacher with two children at a keyboard"></div>

  <div class="frame abs" style="left:141px;top:1667px;width:317px;height:318px"></div>
  <div class="frame-line abs" style="left:160px;top:1686px;width:298px;height:280px;border-right:none;border-bottom:none"></div>
  <div class="photo abs" style="left:204px;top:1728px;width:317px;height:316px;background:linear-gradient(150deg,#e9e3dc,#c59a7c 40%,#3a2c2a 70%,#f2efec)" role="img" aria-label="Two students playing the piano together"></div>

  <div class="programs abs">
    <h2 class="section-title">Our Programs Also Provide Students The Opportunity To</h2>
    <ul>
      <li><svg width="12" height="12" viewBox="0 0 12 12"><circle cx="6" cy="6" r="5" fill="none" stroke="#555"/><path d="M3.5 6l2 2 4-4" fill="none" stroke="#555"/></svg>Participate in large-scale performances.</li>
      <li><svg width="12" height="12" viewBox="0 0 12 12"><circle cx="6" cy="6" r="5" fill="none" stroke="#555"/><path d="M3.5 6l2 2 4-4" fill="none" stroke="#555"/></svg>Perform at Belvina’s many community events on a regular basis.</li>
      <li><svg width="12" height="12" viewBox="0 0 12 12"><circle cx="6" cy="6" r="5" fill="none" stroke="#555"/><path d="M3.5 6l2 2 4-4" fill="none" stroke="#555"/></svg>Access the Metro’s coolest Broadcast stage</li>
      <li><svg width="12" height="12" viewBox="0 0 12 12"><circle cx="6" cy="6" r="5" fill="none" stroke="#555"/><path d="M3.5 6l2 2 4-4" fill="none" stroke="#555"/></svg>Attend Clinics, Masterclasses, and Jam Nights</li>
      <li><svg width="12" height="12" viewBox="0 0 12 12"><circle cx="6" cy="6" r="5" fill="none" stroke="#555"/><path d="M3.5 6l2 2 4-4" fill="none" stroke="#555"/></svg>Access the Belvina Rocks band program. Belvina’s Band Program empowers and electrifies students to come together, create music and confidently hit the stage with their own band identity while having fun and honing their instrument.</li>
      <li><svg width="12" height="12" viewBox="0 0 12 12"><circle cx="6" cy="6" r="5" fill="none" stroke="#555"/><path d="M3.5 6l2 2 4-4" fill="none" stroke="#555"/></svg>Register in our elite teaching program to learn how to pass on the magic and passion of playing the piano to students.</li>
    </ul>
  </div>
  <div class="btn-teal abs" style="left:575px;top:2041px;width:169px;height:35px">CONTACT US TODAY</div>

  <div class="quote-card abs"></div>
  <div class="quote-text abs">“Life is like a piano. What you get out of it depends on how you play it.”</div>
  <div class="quote-name abs">MARIN HOLLOWAY</div>

  <section class="franchise abs">
    <h2 class="section-title">Franchise Opportunities</h2>
    <p>BE PART OF THE BELVINA CONSERVATORY FAMILY</p>
  </section>
  <div class="btn-teal abs" style="left:530px;top:2540px;width:140px;height:35px">KNOW MORE</div>

  <footer class="site-footer abs"></footer>
  <div class="contact-item abs" style="left:190px">
    <svg width="40" height="40" viewBox="0 0 40 40"><circle cx="20" cy="20" r="18" fill="none" stroke="#fff" stroke-width="2"/><path d="M14 12c-2 2-1 6 3 10s8 5 10 3l-3-3-2 1c-2-1-4-3-5-5l1-2z" fill="#fff"/></svg>
    <div><div class="lbl">Call Us Now</div><div class="big">1-800-555-0142</div></div>
  </div>
  <div class="divider abs" style="left:442px"></div>
  <div class="contact-item abs" style="left:478px">
    <svg width="40" height="40" viewBox="0 0 40 40"><circle cx="20" cy="20" r="18" fill="none" stroke="#fff" stroke-width="2"/><path d="M20 10a6 6 0 0 1 6 6c0 5-6 13-6 13s-6-8-6-13a6 6 0 0 1 6-6z" fill="none" stroke="#fff" stroke-width="2"/><circle cx="20" cy="16" r="2" fill="#fff"/></svg>
    <div><div class="lbl" style="font-weight:700">TONES BELVINA</div><div class="lbl" style="font-size:13px">123, Building Name, Street Name<br>State, City XY 123456</div></div>
  </div>
  <div class="divider abs" style="left:756px"></div>
  <div class="contact-item abs" style="left:814px">
    <svg width="40" height="40" viewBox="0 0 40 40"><circle cx="20" cy="20" r="18" fill="none" stroke="#fff" stroke-width="2"/><rect x="12" y="14" width="16" height="12" rx="1" fill="#fff"/><path d="M12 15l8 6 8-6" fill="none" stroke="#000" stroke-width="1.5"/></svg>
    <div><div class="lbl">Email Us:</div><div class="lbl" style="font-size:13px">hello@tonesbelvina-example.com</div></div>
  </div>

  <div class="copy-bar abs"></div>
  <div class="copyright abs">Copyright © 2020 TONES BELVINA. All Rights Reserved.</div>
  <div class="socials abs"><span></span><span></span><span></span><span></span></div>

</div>
</body>
</html>
```